vintage lumivane thank you postcard

I am wanting to use this postcard for my wedding thank you. My theme is: outdoor, rustic, country, vintage, neutral colored. The photo booth at my wedding was in a grain bin on a old victorian couch photos taken with a digital lumivane camera! I want the post card to look like an old fashioned lumivane picture with the border and all. At the bottom saying "thank you" or "Reid and Marta," "Brodwick Wedding", "June 14, 2014," something to that affect. On the back left side leaving room for me to write a personal message thanking them for the help/gift/support. The back right side left for the name and address. I will add a wedding picture of the two of us to the front (from our wedding day). Anything that gives the post card a vintage old time feeling is great!! I have a general idea of what I want but, now I know you guys can take care of the rest for me! :) thank you in advance!! -Marta

Target Market(s)

family, friends - all ages!

Industry/Entity Type

Wedding

Requirements
Must have
• "lumivane photo" look
vintage
"Thank you"
"Reid and Marta"
Nice to have
• June 14, 2014

```html
<!DOCTYPE html>
<html lang="en">
<head>
<meta charset="utf-8">
<title>Brodwick Wedding – Thank You Postcard</title>
<link rel="stylesheet" href="https://fonts.googleapis.com/css2?family=Parisienne&family=Rye&display=swap">
<style>
  :root {
    --backdrop: #ececec;
    --card-tan: #dbb682;
    --card-tan-light: #e3c293;
    --card-edge: #c79a62;
    --frame-white: #f4f5f6;
    --ink-brown: #6e3b1c;
    --ink-grey: #4b4a58;
    --rule-brown: #8a5a34;
    --photo-dark: #2f3a22;
    --photo-mid: #6d7d4a;
    --photo-light: #b8c79a;
  }
  * { box-sizing: border-box; margin: 0; padding: 0; }
  html, body { width: 1200px; height: 1000px; overflow: hidden; }
  body { background: var(--backdrop); position: relative; }

  .card-front, .card-back {
    position: absolute;
    background: radial-gradient(ellipse at 50% 45%, var(--card-tan-light) 0%, var(--card-tan) 70%, var(--card-edge) 100%);
  }

  /* Front */
  .card-front { left: 82px; top: 206px; width: 438px; height: 566px; }
  .instant-frame {
    position: absolute; left: 27px; top: 28px; width: 385px; height: 460px;
    background: var(--frame-white);
  }
  .wedding-photo {
    position: absolute; left: 24px; top: 20px; width: 336px; height: 346px;
    background: linear-gradient(135deg, var(--photo-dark) 0%, var(--photo-mid) 45%, var(--photo-light) 75%, var(--photo-dark) 100%);
  }
  .thank-you {
    position: absolute; left: 70px; top: 372px;
    font-family: "Parisienne", cursive; font-size: 42px; color: var(--ink-grey);
  }
  .couple-names {
    position: absolute; left: 192px; top: 420px;
    font-family: "Parisienne", cursive; font-size: 23px; color: var(--ink-grey);
  }
  .wedding-date {
    position: absolute; left: 0; top: 500px; width: 100%; text-align: center;
    font-family: "Parisienne", cursive; font-size: 21px; color: var(--ink-brown);
  }
  .date-marker { display: inline-block; width: 16px; height: 2px; background: var(--ink-brown); vertical-align: middle; margin: 0 14px; }
  .date-rule {
    position: absolute; left: 128px; top: 542px; width: 182px; height: 1px; background: var(--rule-brown);
  }

  /* Back */
  .card-back { left: 557px; top: 265px; width: 566px; height: 438px; }
  .dashed-border {
    position: absolute; left: 12px; top: 12px; right: 12px; bottom: 12px;
    border: 1px dashed var(--rule-brown); opacity: .6;
  }
  .corner-ornament {
    position: absolute; width: 36px; height: 36px; background: var(--ink-brown); opacity: .35; border-radius: 4px;
  }
  .corner-ornament.top-left { left: 12px; top: 14px; }
  .corner-ornament.top-right { right: 12px; top: 14px; }
  .corner-ornament.bottom-left { left: 12px; bottom: 12px; }
  .corner-ornament.bottom-right { right: 12px; bottom: 12px; }
  .postcard-title {
    position: absolute; left: 0; top: 28px; width: 546px; text-align: center;
    font-family: "Rye", serif; font-size: 31px; color: var(--ink-brown);
  }
  .stamp-box {
    position: absolute; left: 428px; top: 31px; width: 77px; height: 88px;
    border: 1px solid var(--rule-brown);
  }
  .divider-ornament {
    position: absolute; left: 242px; top: 112px; width: 62px; height: 50px;
    background: var(--ink-brown); opacity: .35; border-radius: 50% 50% 8px 8px;
  }
  .divider-line {
    position: absolute; left: 272px; top: 80px; width: 2px; height: 278px; background: var(--rule-brown);
  }
  .divider-foot {
    position: absolute; left: 240px; top: 358px; width: 64px; height: 2px; background: var(--rule-brown);
  }
  .address-label {
    position: absolute; left: 309px; top: 170px;
    font-family: "Parisienne", cursive; font-size: 26px; color: var(--ink-brown);
  }
  .address-lines { position: absolute; left: 312px; top: 230px; width: 193px; }
  .address-line { height: 1px; background: var(--rule-brown); margin-bottom: 24px; }
</style>
</head>
<body>
  <section class="card-front">
    <div class="instant-frame">
      <div class="wedding-photo" role="img" aria-label="Wedding photo of the couple embracing among green trees"></div>
      <div class="thank-you">Thank you</div>
      <div class="couple-names">Reid &amp; Marta</div>
    </div>
    <div class="wedding-date"><span class="date-marker"></span>Brodwick Wedding, 14.6.2014<span class="date-marker"></span></div>
    <div class="date-rule"></div>
  </section>

  <section class="card-back">
    <div class="dashed-border"></div>
    <div class="corner-ornament top-left" role="img" aria-label="Corner flourish ornament"></div>
    <div class="corner-ornament top-right" role="img" aria-label="Corner flourish ornament"></div>
    <div class="corner-ornament bottom-left" role="img" aria-label="Corner flourish ornament"></div>
    <div class="corner-ornament bottom-right" role="img" aria-label="Corner flourish ornament"></div>
    <div class="postcard-title">POSTCARD</div>
    <div class="stamp-box"></div>
    <div class="divider-line"></div>
    <div class="divider-ornament" role="img" aria-label="Scroll ornament on divider"></div>
    <div class="divider-foot"></div>
    <div class="address-label">To</div>
    <div class="address-lines">
      <div class="address-line"></div>
      <div class="address-line"></div>
      <div class="address-line"></div>
      <div class="address-line"></div>
      <div class="address-line"></div>
    </div>
  </section>
</body>
</html>
```